Pages That Sell Services - book cover (front panel only)

I want a book cover (for print and ebook) in a distinctive, quirky style that can be repurposed for podcast artwork too. Full brief supplied.
The book is a practical, accessible handbook for anyone thinking about writing a book to build their business, with a wide range of tips and techniques to help plan, write, publishing and promote a book that’s integrated with your platform and works to build your reputation, network and credibility from day 1.
The target audience is experts in business, particularly owners of SMEs with an established online and offline platform (eg speaking, training, consulting) who want to add a book to take their business to the next level.
I want the design to be strong and distinctive, slightly quirky without being gimmicky, with the focus on typography.

Target Market(s)

Those writing a book based on their expertise to build their business

Industry/Entity Type

Publishing Company

Font styles to use
Serif
Sans Serif
Decorative

Colors

Designer to choose colors to be used in the design.

Requirements
Must have
• Commercially appealing book cover design, with application files and copyright supplied, front panel only, 5.5 x 8.5 inch format. Must work at both full size and thumbnail.
Nice to have
• A distinctive style that could be applied across other products in my portfolio.

```html
<!DOCTYPE html>
<html lang="en">
<head>
<meta charset="utf-8">
<title>Pages That Sell Services – Book Cover</title>
<link rel="stylesheet" href="https://fonts.googleapis.com/css2?family=Amatic+SC:wght@400;700&family=Josefin+Sans:wght@600&display=swap">
<style>
  :root {
    --paper: #ffffff;
    --ink: #141414;
    --label-cyan: #3fc9e4;
    --sub-orange: #f08a2c;
    --sub-red: #e0413d;
    --sub-pink: #d63a6e;
    --sub-purple: #8a4f9e;
    --author-grey: #6f6f6f;
  }
  html, body {
    margin: 0;
    padding: 0;
    overflow: hidden;
    background: var(--paper);
  }
  .cover {
    position: relative;
    width: 775px;
    height: 1200px;
    background: var(--paper);
    overflow: hidden;
  }
  .title-art {
    position: absolute;
    left: 0;
    top: 0;
    width: 775px;
    height: 610px;
  }
  .title-word {
    font-family: "Amatic SC", "Arial Narrow", sans-serif;
    font-weight: 700;
    fill: var(--ink);
  }
  .title-label-box { fill: var(--label-cyan); }
  .title-label {
    font-family: "Amatic SC", "Arial Narrow", sans-serif;
    font-weight: 700;
    fill: var(--ink);
  }
  .subtitle {
    position: absolute;
    left: 90px;
    top: 600px;
    width: 245px;
    margin: 0;
    font-family: "Amatic SC", "Arial Narrow", sans-serif;
    font-weight: 700;
    text-transform: uppercase;
    line-height: 57px;
    font-size: 54px;
  }
  .subtitle span { display: block; white-space: nowrap; }
  .subtitle .line-orange { color: var(--sub-orange); }
  .subtitle .line-red { color: var(--sub-red); }
  .subtitle .line-pink { color: var(--sub-pink); text-align: right; }
  .subtitle .line-purple { color: var(--sub-purple); }
  .illustration {
    position: absolute;
    left: 345px;
    top: 625px;
    width: 360px;
    height: 410px;
  }
  .author {
    position: absolute;
    left: 0;
    right: 0;
    top: 1098px;
    margin: 0;
    text-align: center;
    font-family: "Josefin Sans", "Helvetica", sans-serif;
    font-weight: 600;
    font-size: 48px;
    line-height: 1;
    letter-spacing: 3px;
    color: var(--author-grey);
    text-transform: uppercase;
  }
</style>
</head>
<body>
<main class="cover">
  <svg class="title-art" viewBox="0 0 775 610" aria-label="Pages That Sell Services">
    <rect class="title-label-box" x="227" y="26" width="103" height="62"/>
    <text class="title-label" x="278" y="78" font-size="56" text-anchor="middle" textLength="84" lengthAdjust="spacingAndGlyphs">PAGES</text>

    <text class="title-word" x="80" y="335" font-size="344" textLength="615" lengthAdjust="spacingAndGlyphs">THAT</text>

    <rect class="title-label-box" x="593" y="340" width="150" height="52"/>
    <text class="title-label" x="668" y="384" font-size="52" text-anchor="middle" textLength="72" lengthAdjust="spacingAndGlyphs">SELL</text>

    <text class="title-word" x="88" y="593" font-size="282" textLength="610" lengthAdjust="spacingAndGlyphs">SERVICES</text>
  </svg>

  <p class="subtitle">
    <span class="line-orange">Smart ways to</span>
    <span class="line-red">Shape and draft</span>
    <span class="line-pink">a book</span>
    <span class="line-purple">that wins</span>
    <span class="line-purple">clients for your</span>
    <span class="line-purple">business</span>
  </p>

  <svg class="illustration" viewBox="0 0 360 410" role="img" aria-label="Illustration: open book with a rainbow-coloured head profile rising from its pages">
    <defs>
      <linearGradient id="rainbow-tones" x1="0" y1="0" x2="0.3" y2="1">
        <stop offset="0" stop-color="#f2f2f2"/>
        <stop offset="0.2" stop-color="#e84a8a"/>
        <stop offset="0.4" stop-color="#7a4fc2"/>
        <stop offset="0.6" stop-color="#2db4d8"/>
        <stop offset="0.8" stop-color="#7cc96b"/>
        <stop offset="1" stop-color="#f4c43a"/>
      </linearGradient>
    </defs>
    <rect x="0" y="0" width="360" height="410" fill="url(#rainbow-tones)" opacity="0.55"/>
  </svg>

  <p class="author">Maren Cole</p>
</main>
</body>
</html>
```